Hybrid Seed corn and Soybean Sales business needs a website.

We here at "KT Grain" feel that we need a website to show a very professional side to our customer base. Although no actual ordering will take place on this website, we would like to put Plot and field trail data on the website. Along with a brief page for each of our hybrids and a place for customers to sign up for a newsletter. The company we sell hybrids for is Morvanteld.com... Im not sure how this process works as far as myself updating the information or having the data actually put on the website, but feel free to contact me if you need the information. I will attach the logo for the company, (KT Grain).

Target Market(s)

Farmers, "Producers", Corn and soybean production

Industry/Entity Type

Business

Coding

Coded - Design and coding required

Number of Pages Required

5+ page

Colors
f78f20
ffffff

Requirements
Nice to have
• Similar layout to http://www.morvanteld.com/
• And it would be nice to incorporate our story into the website
• http://www.morvanteld.com/our-story/morvan-today/

```html
<!DOCTYPE html>
<html lang="en">
<head>
<meta charset="utf-8">
<title>KT Grain</title>
<link rel="stylesheet" href="https://fonts.googleapis.com/css2?family=Arimo:ital,wght@0,400;0,700;1,400&family=Squada+One&display=swap">
<style>
:root{
  --orange:#f07b1c;
  --orange-deep:#e8731a;
  --green:#78ae1e;
  --ink:#333333;
  --muted:#777777;
  --rule:#dddddd;
  --panel:#f3f3f3;
  --footer:#1f1f1f;
  --white:#ffffff;
}
*{box-sizing:border-box;margin:0;padding:0}
html,body{width:958px;height:1200px;overflow:hidden;background:var(--white)}
body{position:relative;font-family:"Arimo",Arial,sans-serif;color:var(--ink)}
.abs{position:absolute}
.display{font-family:"Squada One",sans-serif;font-weight:400;letter-spacing:.5px}

.top-rule{left:0;top:0;width:958px;height:2px;background:#555}
.brand{left:78px;top:30px;display:flex;align-items:center;gap:8px}
.brand-dot{width:26px;height:26px;border-radius:50%;background:var(--green)}
.brand-name{font-size:28px;font-weight:700;color:var(--orange);letter-spacing:.5px}
.search{left:686px;top:34px;width:193px;height:31px;border:1px solid #dcdcdc;background:#fafafa;font-size:8px;color:#999;padding:10px 12px}
.search svg{position:absolute;right:10px;top:8px}

.nav{left:0;top:94px;width:958px;height:45px;background:var(--orange);box-shadow:0 2px 3px rgba(0,0,0,.2)}
.nav a{position:absolute;top:0;height:45px;line-height:45px;text-align:center;color:var(--white);font-size:10.5px;font-weight:700;text-decoration:none;border-left:1px solid rgba(255,255,255,.18)}
.nav a.current{background:var(--green);border-left:none}

.hero{left:0;top:140px;width:958px;height:405px;background:radial-gradient(ellipse at 52% 60%,#e39a3a 0%,#b26a24 22%,#6a4a30 48%,#3a2e26 75%,#2a211c 100%)}
.hero-caption{left:78px;top:218px;width:207px;height:197px;background:rgba(90,80,72,.6);padding:22px 28px}
.hero-caption h1{font-size:27px;color:var(--orange);margin-bottom:18px}
.hero-caption p{font-size:10.3px;line-height:16.5px;color:var(--white)}
.hero-btn{left:109px;top:354px;width:73px;height:30px;border:1px solid var(--white);color:var(--white);font-size:10px;line-height:28px;text-align:center}
.hero-arrow{top:472px;width:32px;height:26px;background:rgba(40,35,30,.5)}

.feature{top:574px;width:182px;height:214px;border:1px solid #e2e2e2;background:linear-gradient(#fff,var(--panel));text-align:center;padding:12px 15px 0}
.feature .mark{width:38px;height:38px;border-radius:50%;background:#d9d9d9;margin:0 auto}
.feature h2{font-size:15px;color:var(--orange);margin:14px 0 16px}
.feature p{font-size:8.2px;line-height:16.5px;color:var(--muted);text-align:justify}

.divider{left:78px;top:818px;width:802px;height:1px;background:var(--rule)}
.about-title{left:81px;top:840px;font-size:19px;color:var(--orange)}
.about-photo{left:81px;top:876px;width:217px;height:126px;border:2px solid #eee;background:radial-gradient(ellipse at 25% 85%,#f5c24a 0%,#d06a18 25%,#6a2f12 60%,#2a150c 100%)}
.about-lead{left:329px;top:872px;width:328px;font-style:italic;font-size:10px;line-height:15px;color:#222}
.about-body{left:329px;top:918px;width:328px;font-size:8.2px;line-height:15.2px;color:var(--muted);text-align:justify}
.about-btn{left:328px;top:974px;width:74px;height:30px;border:1px solid var(--orange);color:var(--orange);font-size:10px;line-height:28px;text-align:center}

.newsletter{left:697px;top:842px;width:183px;height:162px;background:var(--orange);border:3px solid #fff;box-shadow:0 0 3px rgba(0,0,0,.3);padding:12px 15px}
.newsletter h2{font-size:15px;color:var(--white)}
.newsletter p{font-size:8.2px;line-height:15px;color:#fff3e6;margin-top:10px}
.newsletter .field{position:absolute;left:14px;top:78px;width:152px;height:29px;background:#fff;font-size:8px;color:#999;padding:9px 11px}
.newsletter .go{position:absolute;left:14px;top:117px;width:59px;height:25px;background:var(--green);color:#fff;font-size:8px;font-weight:700;line-height:25px;text-align:center}

.partner{top:1052px;display:flex;align-items:center;gap:6px;font-size:11px;font-weight:700;color:#333}
.partner i{display:block;width:12px;height:12px;background:var(--orange)}

.footer{left:0;top:1110px;width:958px;height:90px;background:var(--footer);border-top:2px solid var(--orange)}
.footer-links{left:80px;top:1140px;font-size:9px;color:#ccc}
.footer-links span{color:#888;margin:0 6px}
.copyright{left:80px;top:1162px;font-size:9px;color:#ccc}
.social{left:716px;top:1147px;display:flex;gap:12px;font-size:9px;font-weight:700;color:#fff}
</style>
</head>
<body>
<div class="abs top-rule"></div>

<div class="abs brand"><span class="brand-dot"></span><span class="brand-name">KT Grain</span></div>
<div class="abs search">Search Here
  <svg width="14" height="14" viewBox="0 0 14 14"><circle cx="6" cy="6" r="4.5" fill="none" stroke="#bbb" stroke-width="1.6"/><line x1="9.3" y1="9.3" x2="13" y2="13" stroke="#bbb" stroke-width="1.8"/></svg>
</div>

<nav class="abs nav">
  <a class="current" style="left:78px;width:98px">HOME</a>
  <a style="left:177px;width:119px">ABOUT US</a>
  <a style="left:296px;width:114px">SERVICES</a>
  <a style="left:410px;width:102px">SEEDS</a>
  <a style="left:512px;width:95px">NEWS</a>
  <a style="left:607px;width:139px">NEWS LETTER</a>
  <a style="left:746px;width:138px">CONTACT US</a>
</nav>

<div class="abs hero" role="img" aria-label="Hand pouring golden corn kernels into a burlap sack"></div>
<div class="abs hero-caption">
  <h1 class="display">KT GRAIN</h1>
  <p>Lorem ipsum dolor sit amet, conse ctetuer adipiscing elit. Aenean com modo ligula eget dolor.</p>
</div>
<div class="abs hero-btn">Read More</div>
<div class="abs hero-arrow" style="left:808px"><svg width="32" height="26"><polyline points="18,8 13,13 18,18" fill="none" stroke="#ccc" stroke-width="1.2"/></svg></div>
<div class="abs hero-arrow" style="left:844px"><svg width="32" height="26"><polyline points="14,8 19,13 14,18" fill="none" stroke="#ccc" stroke-width="1.2"/></svg></div>

<section>
  <div class="abs feature" style="left:78px"><div class="mark"></div><h2 class="display">QUALITY</h2><p>Lorem ipsum dolor sit amet, consectetuer adipiscing elit. Aenean commodo ligula eget dolor. Aenean massa. Cum sociis natoque penatibus et magnis dis parturient montes, nascetur ridiculus mus. Donec quam felis, ultricies nec,</p></div>
  <div class="abs feature" style="left:285px"><div class="mark"></div><h2 class="display">PRODUCTS</h2><p>Lorem ipsum dolor sit amet, consectetuer adipiscing elit. Aenean commodo ligula eget dolor. Aenean massa. Cum sociis natoque penatibus et magnis dis parturient montes, nascetur ridiculus mus. Donec quam felis, ultricies nec,</p></div>
  <div class="abs feature" style="left:491px"><div class="mark"></div><h2 class="display">MARKETING</h2><p>Lorem ipsum dolor sit amet, consectetuer adipiscing elit. Aenean commodo ligula eget dolor. Aenean massa. Cum sociis natoque penatibus et magnis dis parturient montes, nascetur ridiculus mus. Donec quam felis, ultricies nec,</p></div>
  <div class="abs feature" style="left:697px"><div class="mark"></div><h2 class="display">TECHNOLOGIES</h2><p>Lorem ipsum dolor sit amet, consectetuer adipiscing elit. Aenean commodo ligula eget dolor. Aenean massa. Cum sociis natoque penatibus et magnis dis parturient montes, nascetur ridiculus mus. Donec quam felis, ultricies nec,</p></div>
</section>

<div class="abs divider"></div>

<h2 class="abs about-title display">ABOUT US</h2>
<div class="abs about-photo" role="img" aria-label="Sunset over a crop field with Morvanteld branding"></div>
<p class="abs about-lead">Lorem ipsum dolor sit amet, consectetuer adipiscing elit. Aenean commodo ligula eget dolor. Aenean massa.</p>
<p class="abs about-body">Cum sociis natoque penatibus et magnis dis parturient montes, nascetur ridiculus mus. Donec quam felis, ultricies nec, pellentesque eu, pretium quis, sem. Nulla consequat massa quis enim. Donec pede justo, fringilla vel, aliquet nec.</p>
<div class="abs about-btn">Read More</div>

<div class="abs newsletter">
  <h2 class="display">NEWSLETTER SIGN UP</h2>
  <p>Cum sociis natoque penatibus et magnis dis parturient montes, nascetur</p>
  <div class="field">Email Address</div>
  <div class="go">SIGN UP</div>
</div>

<div class="abs partner" style="left:280px"><i></i>Harlow Agrisciences</div>
<div class="abs partner" style="left:496px"><i></i>Fieldwise</div>
<div class="abs partner" style="left:610px"><i></i>Morvanteld</div>

<footer class="abs footer"></footer>
<div class="abs footer-links">Home<span>/</span>About Us<span>/</span>Services<span>/</span>Seeds<span>/</span>News<span>/</span>News Letter<span>/</span>Contact Us</div>
<div class="abs copyright">© 2015 Copyright KT Grain | All rights reserved</div>
<div class="abs social"><span>Plotter</span><span>Chirp</span><span>Reel</span><span>Feed</span><span>Linkup</span></div>
</body>
</html>
```